Just Listed and Just Sold Post Cards. I have attached copies of what I have had in the past for reference. I have a new company logo attached that needs to be used. Please also include website: www.fernharborfinder.com
email. martawilkes@martawilkeshomes.com
phone 941-555-0173
Target Market(s)
home and land owners
Font styles to use
Sans Serif
Colors
0356a4
Requirements
Must have
- I need a South Gulf Cove Just Listed Card and a Just Sold Card
- Must have My name company name logo website email phone number
- back should read _______. on your block of South Gulf Cove has just SOLD at $________ on _____________________ similar to the one I have attached.
Nice to have
- I like how the attached postcards from before have the shaded picture on the back of the picture on the front. I like to have the aerial as one main photo and the photo with the boat as the other main photo.
- Integrate my Marta Wilkes logo with the TK Meridian logo

```html
<!DOCTYPE html>
<html lang="en">
<head>
<meta charset="utf-8">
<title>Just Listed Postcard – South Gulf Cove</title>
<link rel="stylesheet" href="https://fonts.googleapis.com/css2?family=Oswald:wght@700&family=Raleway:wght@300;400;600;700&display=swap">
<style>
  :root{
    --brand:#0356a4;
    --navy:#0d2140;
    --ground:#1b1b1d;
    --white:#ffffff;
    --grey:#6f7680;
    --orange:#e4701e;
    --panel:rgba(3,86,164,.48);
    --field:rgba(255,255,255,.72);
  }
  *{box-sizing:border-box;margin:0;padding:0}
  html,body{width:1200px;height:1200px;overflow:hidden;background:var(--ground)}
  body{position:relative;font-family:"Raleway",sans-serif}
  .postcard{position:absolute;left:180px;width:840px;height:540px;overflow:hidden;box-shadow:0 10px 30px rgba(0,0,0,.55)}
  .postcard--front{top:40px}
  .postcard--back{top:620px}
  .postcard svg.art{position:absolute;inset:0;width:100%;height:100%}

  /* front */
  .headline{position:absolute;right:36px;top:18px;font-family:"Oswald",sans-serif;font-weight:700;font-size:112px;line-height:1;color:var(--white);letter-spacing:1px;text-shadow:0 3px 8px rgba(0,0,0,.25)}
  .subhead{position:absolute;right:40px;top:150px;font-weight:300;font-size:36px;line-height:1.1;color:var(--white);letter-spacing:1px}
  .agent-mark{position:absolute;right:40px;top:205px;display:flex;align-items:center;gap:8px}
  .agent-mark__dot{width:22px;height:22px;background:var(--navy)}
  .agent-mark__name{font-weight:700;font-size:24px;color:var(--navy);letter-spacing:1px;line-height:1}
  .agent-mark__title{font-weight:700;font-size:10px;color:var(--navy);letter-spacing:2px;text-align:right;margin-top:3px}
  .broker-mark{position:absolute;left:90px;bottom:50px}
  .broker-mark__name{font-weight:700;font-size:28px;line-height:1.1;color:var(--grey);letter-spacing:2px}
  .broker-mark__sub{font-weight:700;font-size:9px;color:var(--grey);letter-spacing:3px;margin-top:4px}

  /* back */
  .logo-panel{position:absolute;left:30px;top:28px;width:270px;height:130px;background:rgba(255,255,255,.85);border-radius:8px;padding:18px 20px}
  .agent-name{display:flex;align-items:center;gap:8px;font-weight:700;font-size:22px;line-height:1.1;color:var(--brand);letter-spacing:1px}
  .agent-name .square{width:18px;height:18px;background:var(--brand);flex:none}
  .agent-role{font-weight:700;font-size:10px;color:var(--orange);letter-spacing:2px;margin:6px 0 0 26px}
  .broker-name{font-weight:700;font-size:18px;line-height:1.1;color:var(--grey);letter-spacing:2px;margin-top:16px}
  .broker-sub{font-weight:700;font-size:7px;color:var(--grey);letter-spacing:2px;margin-top:2px}
  .stamp-box{position:absolute;right:40px;top:28px;width:150px;height:150px;border:1.5px dashed rgba(255,255,255,.8)}
  .message-panel{position:absolute;left:60px;top:190px;width:340px;height:330px;background:var(--panel);border-radius:8px;padding:14px 16px;color:var(--white)}
  .blank{display:inline-block;height:26px;background:var(--field);border-radius:3px;vertical-align:middle}
  .blank--name{width:100%}
  .message{font-size:13px;line-height:1.35;margin-top:8px}
  .price-row{display:flex;align-items:center;gap:6px;margin-top:12px;font-size:13px}
  .price-row .blank{width:110px}
  .invite{font-size:13px;line-height:1.35;margin-top:12px}
  .contact-list{list-style:none;margin-top:22px;font-size:13px}
  .contact-list li{display:flex;align-items:center;gap:8px;margin-top:6px;white-space:nowrap}
  .contact-list svg{width:14px;height:14px;fill:var(--white);flex:none}
</style>
</head>
<body>

<section class="postcard postcard--front">
  <svg class="art" viewBox="0 0 840 540" preserveAspectRatio="none">
    <defs>
      <linearGradient id="aerialTone" x1="0" y1="0" x2="0" y2="1">
        <stop offset="0" stop-color="#4a9be8"/>
        <stop offset="1" stop-color="#6f7c6a"/>
      </linearGradient>
      <linearGradient id="boatTone" x1="0" y1="0" x2="1" y2="1">
        <stop offset="0" stop-color="#3f7fd0"/>
        <stop offset="1" stop-color="#1a3c9a"/>
      </linearGradient>
    </defs>
    <rect width="840" height="540" fill="url(#aerialTone)" role="img" aria-label="Photo area: aerial view of South Gulf Cove canals and home sites"/>
    <polygon points="0,0 840,0 840,230 330,120 0,300" fill="#4aa3f0" opacity=".45"/>
    <polygon points="50,290 330,120 650,270" fill="#2a5cb0" opacity=".3"/>
    <polygon points="390,540 840,220 840,540" fill="url(#boatTone)" role="img" aria-label="Photo area: boat cruising a canal past waterfront homes"/>
    <polygon points="0,540 0,430 190,390 400,540" fill="#ffffff" opacity=".72"/>
  </svg>
  <h1 class="headline">JUST LISTED</h1>
  <p class="subhead">South Gulf Cove</p>
  <div class="agent-mark">
    <span class="agent-mark__dot"></span>
    <div>
      <div class="agent-mark__name">MARTA WILKES</div>
      <div class="agent-mark__title">BROKER ASSOCIATE</div>
    </div>
  </div>
  <div class="broker-mark">
    <div class="broker-mark__name">TK MERIDIAN</div>
    <div class="broker-mark__sub">THORNKEY-MERIDIAN REALTY</div>
  </div>
</section>

<section class="postcard postcard--back">
  <svg class="art" viewBox="0 0 840 540" preserveAspectRatio="none">
    <defs>
      <linearGradient id="backTone" x1="0" y1="0" x2="0" y2="1">
        <stop offset="0" stop-color="#3d85d6"/>
        <stop offset=".5" stop-color="#a9c3d9"/>
        <stop offset="1" stop-color="#f6f8fa"/>
      </linearGradient>
    </defs>
    <rect width="840" height="540" fill="url(#backTone)" role="img" aria-label="Photo area: faded aerial view of South Gulf Cove"/>
  </svg>
  <div class="logo-panel">
    <div class="agent-name"><span class="square"></span>MARTA WILKES</div>
    <div class="agent-role">BROKER ASSOCIATE</div>
    <div class="broker-name">TK MERIDIAN</div>
    <div class="broker-sub">THORNKEY-MERIDIAN REALTY</div>
  </div>
  <div class="stamp-box"></div>
  <div class="message-panel">
    <span class="blank blank--name"></span>
    <p class="message">on Your block of South Gulf Cove<br>has just LISTED</p>
    <div class="price-row">at $ <span class="blank"></span> on <span class="blank"></span></div>
    <p class="invite">Please, contact me if You are interested in buying or selling the property in this area</p>
    <ul class="contact-list">
      <li><svg viewBox="0 0 16 16"><circle cx="8" cy="8" r="7"/></svg>www.fernharborfinder.com</li>
      <li><svg viewBox="0 0 16 16"><path d="M1 3h14v10H1z"/><path d="M1 3l7 5 7-5" fill="none" stroke="#5a8fc4" stroke-width="1.5"/></svg>martawilkes@martawilkeshomes.com</li>
      <li><svg viewBox="0 0 16 16"><path d="M3 1l3 3-2 2c1 2 3 4 5 5l2-2 3 3-2 3C7 14 2 9 1 3z"/></svg>phone 941-555-0173</li>
      <li><svg viewBox="0 0 16 16"><path d="M8 1l7 7h-2v7H9v-5H7v5H3V8H1z"/></svg>PO BOX 418, CORAL BEND, FL 33990</li>
    </ul>
  </div>
</section>

</body>
</html>
```